Corporate brochure Velorin consulting

I am a business law and taxation law firm. I would like to create a super sharp and modern catalogue that really describes our values and the services we offer among other things. It has to be bilingual. I dont want it to look like old fashioned typical law firms. Here are some characteristics of the catalogue:

- size: 8.5 x 11 landscape
- 20 pages in total including the cover page
- bilingual catalogue

Our corporate colors are the ones used in the logo attached.

I already have purchased all of the photos needed for the project.Please see attached document for a detailed description of the project.

I have pictures that I can email you for the project. just email me at jbarlow@velorin-example.ca and I will send the file.

I would just like for you to make available the text boxes on each page and then I will provide the text once Im finished.

Target Market(s)

business owners and professionals

Industry/Entity Type

Business

Font styles to use
Sans Serif

Colors
0692cd
f37122

Requirements
Must have
• bold fonts, very clean white backgrounds, modern and yet very edgy design
• each page should have a large enough area to add text.
• ***I like as the titles: all in large letters and font to use is Adequate,
• Large titles on the left side of page in orange and right side in blue
• for the text: font to be used is asenine
• page numbering should be very visible in the middle of the page left and right and not on bottom or upper corners.
Nice to have
• I like the use of metallic silvers . Not all of the pictures need to be used its the choic of the designer.

```html
<!DOCTYPE html>
<html lang="en">
<head>
<meta charset="utf-8">
<title>Velorin Consulting – Services Spread</title>
<link href="https://fonts.googleapis.com/css2?family=Oswald:wght@400;500&family=Open+Sans:wght@400;600&family=Lato:wght@700;900&display=swap" rel="stylesheet">
<style>
  :root{
    --orange:#f37122;
    --blue:#0692cd;
    --ink:#4a4a4a;
    --title:#555555;
    --rule:#cfcfcf;
    --bar:#3e3e3e;
    --paper:#ffffff;
    --backdrop:#e4e4e4;
  }
  *{margin:0;padding:0;box-sizing:border-box}
  html,body{width:1200px;height:638px;overflow:hidden;background:var(--backdrop)}
  .spread{position:absolute;left:55px;top:120px;width:1090px;height:400px;background:var(--paper);box-shadow:0 6px 18px rgba(0,0,0,.18);overflow:hidden}
  .page{position:absolute;top:0;width:545px;height:400px}
  .page--left{left:0}
  .page--right{left:545px}
  .top-bar{position:absolute;top:0;height:6px;background:var(--bar)}
  .page--left .top-bar{left:0;width:400px}
  .page--right .top-bar{right:0;width:400px}
  .section-tag{position:absolute;top:6px;height:22px;padding:0 9px;background:var(--blue);color:#fff;font:700 8.5px/22px "Lato",sans-serif;letter-spacing:.4px}
  .page--left .section-tag{left:30px}
  .page--right .section-tag{right:30px}
  .content{position:absolute;top:34px;width:355px;color:var(--ink);font:400 6.1px/1.5 "Open Sans",sans-serif}
  .page--left .content{left:30px}
  .page--right .content{left:175px}
  .page-title{font:400 23px/1 "Oswald",sans-serif;color:var(--title);text-transform:uppercase;padding:6px 0 8px;border-bottom:1px solid var(--rule);border-top:1px solid var(--rule);margin-bottom:10px}
  .intro{margin-bottom:8px}
  .sub{font:900 8.6px/1.2 "Lato",sans-serif;color:var(--orange);text-transform:uppercase;margin:6px 0 1px}
  .content p + p{margin-top:5px}
  .photo-main{position:absolute;left:413px;top:36px;width:264px;height:264px;border-radius:50%;border:4px solid var(--blue);box-shadow:0 0 0 4px #fff,0 0 0 5px #d7e9f3;background:radial-gradient(circle at 50% 35%,#f4e1cf 0 26%,#6fb6e3 27%,#2d8fd0 70%,#1d6fb0 100%)}
  .photo-sub{position:absolute;left:485px;top:216px;width:120px;height:120px;border-radius:50%;border:4px solid var(--blue);box-shadow:0 0 0 3px #fff;background:radial-gradient(circle at 50% 50%,#e9eef2 0 30%,#9fb4c6 65%,#56708a 100%)}
  .footer{position:absolute;left:0;top:358px;width:1090px;height:40px;background:var(--orange)}
  .page-num{position:absolute;top:5px;width:30px;height:30px;border-radius:50%;background:#fff;color:var(--orange);font:700 12px/30px "Lato",sans-serif;text-align:center}
  .footer-line{position:absolute;top:0;font:400 10px/40px "Open Sans",sans-serif;color:#fff;white-space:nowrap}
  .footer-line strong{font-weight:600}
  .brand{position:absolute;top:0;font:600 10px/40px "Open Sans",sans-serif;color:#fff;letter-spacing:.5px}
  .gutter{position:absolute;left:530px;top:0;width:30px;height:400px;background:linear-gradient(90deg,rgba(0,0,0,0),rgba(0,0,0,.12) 50%,rgba(0,0,0,0))}
</style>
</head>
<body>
<div class="spread">
  <section class="page page--left">
    <div class="top-bar"></div>
    <div class="section-tag">SERVICES</div>
    <div class="content">
      <h1 class="page-title">Asset Protection</h1>
      <p class="intro">In case of litigation or legal disputes, our lawyers can help protect your personal assets against seizure by a potential creditor.</p>
      <h2 class="sub">Incorporation</h2>
      <p>A corporation possesses its own legal personality separate from that of its shareholders. By shielding personal assets from a corporation's creditors, shareholders obtain asset protection and peace of mind while running a business.</p>
      <h2 class="sub">Holding Corporation</h2>
      <p>This strategy allows for the separation of a corporation's activities into two separate entities: the operating company and the holding company. The operating company handles day-to-day operations of the business while the holding company contains the business' investments and excess cash. In case of a lawsuit, assets found in the holding company can be protected from court claims.</p>
      <h2 class="sub">Loans between corporations guaranteed by a moveable hypothec</h2>
      <p>This strategy allows for the operating company's assets to be protected in case of a legal action. Instead of borrowing money from a bank, the operating company borrows working capital from the holding company. In exchange, the operating company grants a hypothec on the universality of its property (trucks, equipment etc.) in favour of the holding company.</p>
      <p>Given that the holding company has a hypothec on the property of the operating company, the property of the latter is protected from seizure by creditors. This is because the hypothec held by the holding company would rank ahead of any other creditor's rank.</p>
      <h2 class="sub">Asset protection trust ( or principal residence trust)</h2>
      <p>This inter vivos trust is created by drafting a private document and then transferring valuable real real estate into it such as a principal residence. Since a trust has a separate legal personality distinct from the person who created it, should a lawsuit occur, creditors will not be able to seize property held in the trust.</p>
      <p>This strategy is useful and often recommended for individuals with no mortgage on their home or who have at least $350,000 of equity in their residence.</p>
    </div>
  </section>

  <section class="page page--right">
    <div class="top-bar"></div>
    <div class="section-tag">SERVICES</div>
    <div class="content" lang="fr">
      <h1 class="page-title">Protection d'actifs</h1>
      <p class="intro">En cas de poursuites, nous pouvons vous aider à protéger vos biens personnels contre vos créanciers par la mise en place de certaines stratégies légales:</p>
      <h2 class="sub">L'incorporation</h2>
      <p>La société par actions dispose d'un patrimoine distinct de son actionnaire, ce qui protège ce dernier, parce qu'il n'a pas à rembourser personnellement les dettes de sa société. Par conséquent, ses biens personnels sont généralement à l'abri des créanciers.</p>
      <h2 class="sub">La société de gestion (ou de portefeuille)</h2>
      <p>Cette stratégie permet de séparer, par l'entremise d'une société par actions distinctes, les activités courantes de la société par action opérante des investissements de l'actionnaire (portefeuille d'actions, fonds mutuels, immobilier).</p>
      <h2 class="sub">Le prêt entre sociétés garanti par hypothèque</h2>
      <p>Cette stratégie vise à protéger les biens de la société opérante en cas de poursuites. Au lieu d'emprunter de l'argent à une banque, la société opérante emprunte à la société de gestion les liquidités du fonds de roulement. En échange, la société de gestion enregistre une hypothèque universelle sur les biens de la société opérante (camions, équipements, etc.).</p>
      <p>Étant donné que la société de gestion détient une hypothèque sur l'universalité des biens de la société opérante, les biens de cette dernière sont protégés contre ses créanciers, parce que la dette de la société de gestion est prioritaire à celle des autres créanciers.</p>
      <h2 class="sub">La fiducie de protection d'actifs</h2>
      <p>Cette fiducie entre vifs est créée suite à la rédaction d'un document juridique sous seing privé. Elle possède un patrimoine juridique distinct de l'entrepreneur. Généralement, en cas de poursuites, les créanciers ne pourront pas avoir accès aux biens détenus par la fiducie.</p>
      <p>Cette stratégie est utile lorsque votre résidence est libre de dettes ou qu'une équité d'au moins 350 000$ y est accumulée.</p>
    </div>
  </section>

  <div class="photo-main" role="img" aria-label="Photo: cupped hands sheltering a paper cut-out of a family and house against a blue sky"></div>
  <div class="photo-sub" role="img" aria-label="Photo: a person's hands held protectively over a small house shape"></div>

  <footer class="footer">
    <div class="page-num" style="left:28px">14</div>
    <div class="footer-line" style="left:180px"><strong>VELORIN CONSULTING</strong> - A Creative Law Firm</div>
    <div class="brand" style="left:473px">VELORIN</div>
    <div class="brand" style="left:570px">VELORIN</div>
    <div class="footer-line" style="left:740px"><strong>VELORIN CONSEILS</strong> - Une Vision D'affaires</div>
    <div class="page-num" style="left:1043px">15</div>
  </footer>
  <div class="gutter"></div>
</div>
</body>
</html>
```